Systems and Technology Consultants - Website

Design & Build a website for a new company which operates in the Systems and Technology space for Transportation, Government and Commercial sectors.

Overall design should be minimalist in nature.
Should also have a feed that provides news and event updates on the main page.
Logo has already been awarded and should be incorporated into the site.

We like the overall layout, functionality and simplicity of the below sites. Submitted designs could be similar to or a combination of the aspects on these sites, or perhaps a whole different concept - we are open to new ideas.
Vortrane.com
Merp.it

Update 1 Dated 27 May 2014

All I am moving away from the Merp.it website and would like it to be more aligned with Vortrane.com not only in layout but in functionality. I will be extending the deadline of this design brief for two weeks to incorporate additional requirements and will add addtional funding to the project.

Apologies for not having more information available to provide but with so many submissions its getting confusing.

Thanks Dermot
Updates

Please note that the brief has been updated and the deadline has been extended.

Important: We will need two language versions of the website, English and Arabic; the website is hosted on HostPeak

Hello All, Thank you for your submissions. We have narrowed it down to the final 6 designers and I just wanted to take a moment and provide a bit of feedback regarding the concepts that we like and the modifications we are looking for. First, let me mention some of the design functions we like. - At the top of the homepage we really like the "region" or "language" tab so that the website can be viewed in both English and Arabic. - We like the homepage to have clear color variation so that the different sections of the homepage are distinct. Additionally, we like the bottom portion of the homepage to be in red. We feel that draws attention to our contact information. Again, we would like the colors to integrate black, gray-scale, red, etc. - Having a search tab at the top of the home page, or integrated into the main image, so that the site is easy to navigate. - We especially like the main image to have the scrolling tabs at the bottom so it is easy to browse the services offered (Consultancy, Solutions Architecture, Masters Systems Integration, Independent Design Review). - In regards to the services offered tab we really like the idea that a few people presented that have the outside of our logo with an icon in the middle of consultancy, solutions, etc., etc. Secondly, as mentioned in our brief we really enjoy the design of vortrane site. Specially, we enjoy the strong iconic images they use, the way the tabs at the top scroll easily, and contact us page that generates an email. Lastly, I've included some photos of the concept we have been working on. What we are trying to demonstrate is how our company offers a range of services that are essentially linked together. We provide individual services that when combined present the full service package. We would like this concept to be integrated into the over concept of our website. Please feel free to ask for clarification of any of the above points or contact us if you have any additional questions. We appreciate all of your hard work and are very excited to see the updated designs. Best, Miriam Dowbrook Plenvaro Senior Program Manager miriam.dowbrook@plenvaro-mail.com

Industry/Entity Type

Government

Font styles to use
Serif
Sans Serif

Requirements
Must have
• Must work on/adapt to various/mobile devices (responsive)
Must be simple and straightforward
Colors should be in line/matching with logo
2 language versions: English and Arabic (no Thai)
Services should be the first group/row of items after/below the main image
Note: the website will be hosted by hostpeak
Nice to have
• Submit feedback form
What's New section
The banner at the bottom of the site should not be too large; we would like a narrow one more
It would be nice if the header/top banner (with Home, About, etc. tabs) could stay in place as you scroll down (like Vortrane and Chatterly)
We will likely only use one image with a Company slogan on the Home page rather than a carousel of images to rotate through
Should not have
• This is the existing website: http://www.plenvaro-example.org
We do not like the animation, the way the banner icons/titles bounce
Not simple enough, we don't like the functionality or how pages load so slowly
We do not like the logo centered - it should be at the left
The banner and its tabs should not be towards the right, we would like them to be centered, to go all the way across and to be below the logo

```html
<!DOCTYPE html>
<html lang="ar" dir="rtl">
<head>
<meta charset="utf-8">
<title>Plenvaro</title>
<link href="https://fonts.googleapis.com/css2?family=Noto+Kufi+Arabic:wght@400;600;700&family=Noto+Sans+Arabic:wght@400;600&display=swap" rel="stylesheet">
<style>
:root{
  --white:#ffffff;
  --ink:#2b3038;
  --dark:#2e333a;
  --footer:#2a2d33;
  --sand:#e6dc8c;
  --sand-deep:#d9cd72;
  --paper:#efeee9;
  --mist:#f4f4f2;
  --red:#d0352b;
  --muted:#6b6e73;
  --line:#cfcfcf;
}
*{box-sizing:border-box;margin:0;padding:0}
html,body{width:694px;height:1200px;overflow:hidden}
body{font-family:"Noto Sans Arabic",sans-serif;color:var(--ink);background:var(--white);direction:rtl}
h2{font-family:"Noto Kufi Arabic",sans-serif;font-weight:600}

.site-header{height:46px;display:flex;align-items:center;justify-content:center;gap:30px;background:var(--white);font-size:11px}
.site-header a{color:var(--ink);text-decoration:none}
.brand{display:flex;flex-direction:column;align-items:center;font-family:"Noto Kufi Arabic",sans-serif;font-size:10px;font-weight:600;letter-spacing:1px;color:var(--dark);margin:0 18px}
.brand-mark{width:18px;height:18px;border:2px solid var(--dark);border-radius:50%;margin-bottom:2px}

.hero{height:254px;position:relative;background:linear-gradient(180deg,#8c97a6 0%,#b7bec7 35%,#c7c4bd 60%,#6f7780 85%,#4a525c 100%);display:flex;align-items:center;justify-content:center}
.hero h1{font-family:"Noto Kufi Arabic",sans-serif;font-weight:600;font-size:30px;color:var(--white);margin-top:-20px}

.mission{height:162px;background:var(--dark);color:var(--white);text-align:center;padding-top:40px}
.mission h2{font-size:22px;margin-bottom:12px}
.mission p{font-size:10.5px;line-height:1.7;color:#d7d9dc}

.about{height:213px;background:var(--sand);position:relative;padding:30px 60px 0 220px}
.about h2{font-size:20px;text-align:center;margin-bottom:12px;margin-right:-160px}
.about p{font-size:9.5px;line-height:1.75;text-align:right}
.company-photo{position:absolute;left:46px;top:56px;width:116px;height:116px;border-radius:50%;background:#efefef;border:6px solid var(--sand-deep);display:flex;align-items:center;justify-content:center;font-size:14px;color:var(--muted)}

.offices{height:215px;background:linear-gradient(180deg,var(--paper) 0%,#e6e3da 100%);text-align:center;padding-top:24px;position:relative}
.offices h2{font-size:20px;margin-bottom:8px}
.offices .lead{font-size:9.5px;line-height:1.7;color:var(--ink)}
.office-list{display:flex;justify-content:center;gap:110px;margin-top:18px}
.office{display:flex;align-items:flex-start;gap:8px;text-align:right}
.office h3{font-family:"Noto Kufi Arabic",sans-serif;font-size:18px;font-weight:600;line-height:1.2}
.office p{font-size:8.5px;line-height:1.6;color:var(--muted)}

.contact{height:185px;background:var(--mist);text-align:center;padding-top:22px}
.contact h2{font-size:20px;margin-bottom:6px}
.contact .lead{font-size:9.5px;line-height:1.6;margin-bottom:10px}
.contact-form{width:490px;margin:0 auto;display:grid;grid-template-columns:1fr 1fr;gap:8px}
.field{height:22px;background:var(--white);border:1px solid var(--line);font-size:9px;color:var(--muted);text-align:right;padding:4px 8px}
.field.message{grid-column:1/3;height:50px}

.site-footer{height:125px;background:var(--footer);color:#c9cbce;display:flex;justify-content:space-between;padding:26px 60px 0;font-size:10px}
.site-footer ul{list-style:none;line-height:1.75}
.social{direction:ltr;text-align:left;font-weight:600;color:var(--white);font-size:11px}
</style>
</head>
<body>
<header class="site-header">
  <a href="#">من نحن؟</a>
  <a href="#">شركاتنا</a>
  <div class="brand"><span class="brand-mark"></span>PLENVARO</div>
  <a href="#">مقراتنا</a>
  <a href="#">إتصل بنا</a>
  <a href="#">خارطة الموقع</a>
</header>

<section class="hero" role="img" aria-label="صورة بانورامية لأفق مدينة حديثة على الواجهة البحرية">
  <h1>معاً تتحقق أهدافك.</h1>
</section>

<section class="mission">
  <h2>هدفنا.. نجاحكم.</h2>
  <p>نوفر لكم أحدث التقنيات والخبرات في مجال الهندسة والمعلوماتية لتطوير من أداء مشاريعكم<br>نعمل من إنشاء تخطيط متنوع وتنظيم الجهود لتحقيق أهدافك ونقل أفكاركم إلى أرض الواقع.</p>
</section>

<section class="about">
  <h2>من نحن؟</h2>
  <p>نحن شركة إقليمية تعمل في قطاع الأنظمة والتقنيات، نقدم خدمات الاستشارات وتكامل الأنظمة لمشاريع النقل والقطاع الحكومي والقطاع التجاري. نعمل مع شركائنا لتقديم حلول متكاملة تبدأ من الفكرة وتنتهي بالتنفيذ والتشغيل، ونؤمن بأن الخدمات المترابطة تصنع قيمة أكبر لعملائنا. يضم فريقنا خبراء في التصميم والمراجعة المستقلة وهندسة الحلول، ونسعى دائماً إلى تقديم أفضل الحلول والتقنيات.</p>
  <div class="company-photo" role="img" aria-label="صورة للشركة">صورة للشركة</div>
</section>

<section class="offices" aria-label="مقراتنا">
  <h2>مقراتنا</h2>
  <p class="lead">تتواجد مكاتبنا في عدد من المدن الرئيسية لخدمة عملائنا في المنطقة<br>ويسعدنا استقبالكم في أي من مقراتنا خلال أوقات العمل الرسمية.</p>
  <div class="office-list">
    <div class="office">
      <svg width="26" height="38" viewBox="0 0 26 38" aria-hidden="true"><path d="M13 0C5.8 0 0 5.8 0 13c0 9.5 13 25 13 25s13-15.5 13-25C26 5.8 20.2 0 13 0z" fill="var(--red)"/><circle cx="13" cy="13" r="5" fill="#8e1f18"/></svg>
      <div><h3>بانكوك</h3><p>مبنى فالورا، الطابق 7<br>18 شارع السنديان<br>بانكوك - تايلاند</p></div>
    </div>
    <div class="office">
      <svg width="26" height="38" viewBox="0 0 26 38" aria-hidden="true"><path d="M13 0C5.8 0 0 5.8 0 13c0 9.5 13 25 13 25s13-15.5 13-25C26 5.8 20.2 0 13 0z" fill="var(--red)"/><circle cx="13" cy="13" r="5" fill="#8e1f18"/></svg>
      <div><h3>الدوحة</h3><p>مجمع الريم، مكتب 204<br>شارع الياسمين<br>الدوحة - قطر</p></div>
    </div>
  </div>
</section>

<section class="contact">
  <h2>إتصل بنا</h2>
  <p class="lead">تفضل بإرسال استفساراتك أو ملاحظاتك وسيقوم فريقنا بالرد عليك<br>في أقرب وقت ممكن.</p>
  <form class="contact-form">
    <div class="field">الإسم الكامل</div>
    <div class="field">البريد الإلكتروني</div>
    <div class="field message">الرسالة</div>
  </form>
</section>

<footer class="site-footer">
  <ul>
    <li>من نحن؟</li>
    <li>شركاتنا</li>
    <li>أين تجدنا؟</li>
    <li>إتصل بنا</li>
  </ul>
  <ul>
    <li>صفحتنا</li>
    <li>شركاؤنا</li>
    <li>خطط المستقبل</li>
    <li>خارطة الموقع</li>
  </ul>
  <ul class="social">
    <li>Chatterly</li>
    <li>Chirpline</li>
    <li>Snapgrid</li>
  </ul>
</footer>
</body>
</html>
```